Beautiful Simple and Clean WEbsite for Life Coach

Looking for a simple clean site website for life coach for educators. A home page will have an embedded opt-in form, menu bar will be
Work With Me - page for my coaching program and link to online calendar for booking
PRAISE - testimonials
ABOUT
PODCAST
I can supply images and a site I would like it modeled after is https://petrawendt.com/
My current website at www.dorabeckett.com is too dark. I am looking for the white space, pink and magenta. Feel free to use images from the site

Industry/Entity Type

Life Coaching

Number of Pages Required

4 page

Font styles to use
Serif

Colors
E54698
E96AAD
F1A4CE
F9D9EA
FCEFF6

Requirements
Must have
• See attached files for must-haves, Lots of white space, opt-in from for freebie is the most prominent on home page
Nice to have
• refer to Petra Wendt websites
Should not have
• dark colors, any balck background

```html
<!DOCTYPE html>
<html lang="en">
<head>
<meta charset="utf-8">
<title>Dora Beckett – Life Coach for Educators</title>
<link href="https://fonts.googleapis.com/css2?family=Playfair+Display:wght@400;500&family=Roboto:wght@400;500&display=swap" rel="stylesheet">
<style>
:root{
  --pink:#e9a3ae;
  --pink-deep:#d98b98;
  --blush:#f8e1db;
  --sage:#d8e0dc;
  --ink:#2b2b2b;
  --muted:#8a8a8a;
  --mauve:#8c6a70;
  --white:#ffffff;
}
*{box-sizing:border-box;margin:0;padding:0}
html,body{width:1200px;height:4124px;overflow:hidden;background:var(--white)}
body{position:relative;font-family:"Roboto",sans-serif;color:var(--muted)}
.abs{position:absolute}
.serif{font-family:"Playfair Display",serif}
.btn{position:absolute;background:var(--pink);color:var(--white);border-radius:30px;font:500 13px "Roboto",sans-serif;text-transform:uppercase;display:flex;align-items:center;justify-content:center;letter-spacing:.3px}
.brand{font:400 34px "Playfair Display",serif;color:var(--mauve)}
.nav{position:absolute;top:42px;left:534px;display:flex;gap:36px;font:500 13px "Roboto",sans-serif;color:var(--mauve)}
.photo{position:absolute}
.h2{font:500 34px "Playfair Display",serif;color:var(--ink);text-transform:uppercase}
.center{left:0;width:1200px;text-align:center}
.body-text{font-size:15px;line-height:27px;color:var(--muted)}
.band-pod{top:2120px;height:588px;left:0;width:1200px;background:linear-gradient(180deg,#e9a3a9,#dd979f)}
.pod-card{position:absolute;top:2264px;width:231px;height:366px;background:var(--white);border-radius:4px}
.pod-card .photo{left:6px;top:6px;width:219px;height:152px}
.pod-meta{position:absolute;top:176px;width:100%;text-align:center;font-size:10px;color:var(--pink-deep)}
.pod-title{position:absolute;top:200px;left:12px;right:12px;text-align:center;font:500 15px/21px "Roboto",sans-serif;color:var(--ink)}
.pod-text{position:absolute;top:260px;left:14px;right:14px;text-align:center;font-size:10.5px;line-height:20px;color:var(--muted)}
.pod-icons{position:absolute;top:322px;width:100%;display:flex;justify-content:center;gap:8px}
.pod-icons span{width:20px;height:20px;border-radius:50%;background:#cfd6d2}
.pod-icons span:first-child{background:var(--pink)}
.blog-card{position:absolute;top:2873px;width:300px;height:417px;background:var(--white);box-shadow:0 4px 22px rgba(0,0,0,.12);border-radius:4px}
.blog-card .photo{left:7px;top:7px;width:286px;height:210px}
.blog-date{position:absolute;top:236px;width:100%;text-align:center;font-size:12px;color:var(--mauve)}
.blog-title{position:absolute;top:262px;left:36px;right:36px;text-align:center;font:500 16px/25px "Roboto",sans-serif;color:var(--mauve);text-transform:uppercase}
.blog-text{position:absolute;top:318px;left:26px;right:26px;text-align:center;font-size:14px;line-height:25px;color:var(--muted)}
.blog-more{position:absolute;top:378px;width:100%;text-align:center;font:500 13px "Roboto",sans-serif;color:var(--pink-deep);text-transform:uppercase}
.field{position:absolute;background:var(--white);border-radius:3px;font-size:14px;color:#555;padding:15px 17px}
.foot-nav{top:3940px;display:flex;justify-content:center;gap:26px;font:500 15px "Roboto",sans-serif;color:#666}
.socials{top:4014px;display:flex;justify-content:center;gap:6px}
.socials span{width:30px;height:30px;border-radius:50%;background:#cfd6d2}
.socials span:first-child{background:var(--pink)}
</style>
</head>
<body>

<!-- Header -->
<div class="abs brand" style="left:112px;top:28px">Dora Beckett</div>
<nav class="nav"><span>WORK WITH ME</span><span>PRAISE</span><span>ABOUT</span><span>PODCAST</span></nav>
<div class="btn" style="left:960px;top:27px;width:128px;height:48px">Contact</div>

<!-- Hero -->
<div class="photo" role="img" aria-label="Portrait of the coach smiling outdoors" style="left:429px;top:105px;width:771px;height:599px;background:linear-gradient(120deg,#3f4a36 0%,#7c7356 45%,#b8a58a 60%,#5b4a3c 100%)"></div>
<div class="abs" style="left:112px;top:198px;width:488px;height:412px;background:var(--blush);border-radius:8px"></div>
<h1 class="abs serif" style="left:162px;top:258px;font-weight:500;font-size:37px;line-height:48px;color:var(--ink)">LIFE COACH FOR<br>EDUCATORS</h1>
<p class="abs" style="left:162px;top:374px;width:400px;font-size:18px;line-height:29px;color:#7a7a7a">DISCOVER the secrets on how to prioritize the items on an overwhelming to-do list to get the job done successfully.</p>
<div class="btn" style="left:162px;top:490px;width:141px;height:49px">Get Started</div>

<!-- Work with me -->
<section class="abs" style="left:0;top:704px;width:1200px;height:574px;background:var(--sage)"></section>
<div class="abs" style="left:112px;top:808px;width:445px;height:367px;background:var(--white);border-radius:6px;box-shadow:0 4px 14px rgba(0,0,0,.12)"></div>
<div class="photo" role="img" aria-label="Coaching session between two women" style="left:120px;top:816px;width:429px;height:351px;background:linear-gradient(90deg,#d9c7b4,#f1ebe3 55%,#b5a08c)"></div>
<h2 class="abs h2" style="left:620px;top:808px">Work With Me</h2>
<p class="abs body-text" style="left:620px;top:874px;width:468px;text-align:justify">Lorem ipsum dolor sit amet, consectetur adipiscing elit, sed do eiusmod tempor incididunt ut labore et dolore magna aliqua. Ut enim ad minim veniam, quis nostrud exercitation ullamco lab oris nisi ut aliquip ex ea commodoea.</p>
<p class="abs body-text" style="left:620px;top:998px;width:468px;text-align:justify">Sed ut perspiciatis unde omnis iste natus error sit voluptatem accusantium doloremque laudantium, totam rem aperiam, eaque ipsa quae ab illo inventorea.</p>
<div class="btn" style="left:620px;top:1117px;width:138px;height:49px">Read More</div>

<!-- About -->
<h2 class="abs h2 center" style="top:1384px">About Me</h2>
<p class="abs serif center" style="top:1430px;font-size:35px;color:var(--pink-deep)">Hi, I'm Dora Beckett!</p>
<p class="abs body-text" style="left:120px;width:960px;top:1496px;text-align:center">I'm a Life Coach.&nbsp; I am also a retired Elementary School Principal who loves other educators and everything in education. In my coaching practice, I empower my clients with simple survival skills to succeed at their school and in their life.</p>
<p class="abs body-text" style="left:112px;top:1657px;width:468px;text-align:justify">They have more time, less stress, and yell less. If you would like to learn more about how to manage stress and overwhelm, and how to feel better no matter what the circumstances I am your gal. I'm a "tell it like it is" Texan with a warm heart for anyone feeling overwhelmed by life, who wishes to have different results in their life. I have a weakness for public education, hardware stores, yummy art supplies,&nbsp; and the poems of Clara Winslow. Lovely to meet you!</p>
<div class="btn" style="left:112px;top:1908px;width:137px;height:49px">Read More</div>
<svg class="abs" style="left:640px;top:1585px" width="460" height="450" viewBox="0 0 460 450">
  <circle cx="232" cy="220" r="216" fill="#d8e0dc"/>
  <circle cx="224" cy="230" r="216" fill="none" stroke="#e9a3ae" stroke-width="3" stroke-dasharray="740 700" transform="rotate(60 224 230)"/>
</svg>
<div class="photo" role="img" aria-label="Coach seated in a field of tall dry grass" style="left:661px;top:1608px;width:412px;height:412px;border-radius:50%;background:radial-gradient(circle at 50% 45%,#e8e2d6 0%,#b9a88a 45%,#7d6a4f 100%)"></div>

<!-- Podcast -->
<section class="abs band-pod"></section>
<h2 class="abs serif center" style="top:2186px;font-size:38px;font-weight:500;color:var(--white)">PODCAST</h2>

<div class="pod-card" style="left:112px">
  <div class="photo" role="img" aria-label="Host smiling at an airport" style="background:linear-gradient(135deg,#9fc3dc,#e7c9a4 60%,#d9a65a)"></div>
  <div class="pod-meta">7/20/2021 &nbsp;|&nbsp; 21 min</div>
  <div class="pod-title">Latest Episode<br>Doable To-Do List 101</div>
  <div class="pod-text">Today's episode is all about the to-do list. More specifically, the doable to-do list. As educators, we have...</div>
  <div class="pod-icons"><span></span><span></span><span></span></div>
</div>
<div class="pod-card" style="left:360px">
  <div class="photo" role="img" aria-label="Person writing a journal by the sea at sunset" style="background:linear-gradient(180deg,#f0c9a6,#e6b39a 60%,#b58a80)"></div>
  <div class="pod-meta">6/22/2021 &nbsp;|&nbsp; 17 min</div>
  <div class="pod-title">Get Your Groove Back With Journaling</div>
  <div class="pod-text">This episode is all about journaling. Do you ever think to yourself, why can't I just simplify my teacher life?...</div>
  <div class="pod-icons"><span></span><span></span><span></span></div>
</div>
<div class="pod-card" style="left:609px">
  <div class="photo" role="img" aria-label="Couple in hats on a hiking trail" style="background:linear-gradient(180deg,#7f9a62,#b8b08c 55%,#6b7c8c)"></div>
  <div class="pod-meta">6/22/2021 &nbsp;|&nbsp; 25 min</div>
  <div class="pod-title">Practice Catching Those Thoughts</div>
  <div class="pod-text">So many teachers complain about how difficult it is to balance work and home. Sadly, work takes a...</div>
  <div class="pod-icons"><span></span><span></span><span></span></div>
</div>
<div class="pod-card" style="left:857px">
  <div class="photo" role="img" aria-label="Host recording at a microphone" style="background:linear-gradient(135deg,#e9eef1,#c9d1d6 55%,#8d969c)"></div>
  <div class="pod-meta">6/17/2021 &nbsp;|&nbsp; 24 min</div>
  <div class="pod-title">Welcome to the Show</div>
  <div class="pod-text">In this first episode of Bright Teacher, Bright Life host Dora Beckett speaks to overwhelmed...</div>
  <div class="pod-icons"><span></span><span></span><span></span></div>
</div>

<!-- Blog -->
<h2 class="abs h2 center" style="top:2790px;font-size:36px">Latest Blog</h2>
<div class="blog-card" style="left:128px">
  <div class="photo" role="img" aria-label="Counselling conversation in a bright office" style="background:linear-gradient(90deg,#e9e6e0,#bfcbe0 50%,#5a4a40)"></div>
  <div class="blog-date">04 FEB 2022</div>
  <div class="blog-title">Why Are We Hard On Ourselves?</div>
  <div class="blog-text">"The Inner Critic Speaks" is a phrase I hear from many teachers</div>
  <div class="blog-more">Read More &rarr;</div>
</div>
<div class="blog-card" style="left:450px">
  <div class="photo" role="img" aria-label="Friends gathered in a warm living room" style="background:linear-gradient(90deg,#6b4e3e,#d9c4b0 50%,#7a5c48)"></div>
  <div class="blog-date">13 DEC 2021</div>
  <div class="blog-title">Build Great Relationships For The Holidays</div>
  <div class="blog-text">Are you having either one of these holiday thoughts? "I can't wait</div>
  <div class="blog-more">Read More &rarr;</div>
</div>
<div class="blog-card" style="left:771px">
  <div class="photo" role="img" aria-label="Woman resting among green leaves" style="background:linear-gradient(135deg,#2f4a3e,#7d9a86 55%,#c9b9a8)"></div>
  <div class="blog-date">28 NOV 2021</div>
  <div class="blog-title">Tis The Season Of<br>"Over-Ing."</div>
  <div class="blog-text">So excited that you are here and for the opportunity to share</div>
  <div class="blog-more">Read More &rarr;</div>
</div>

<!-- Contact -->
<section class="abs" role="img" aria-label="Soft misty backdrop of a person with raised arms" style="left:0;top:3395px;width:1200px;height:417px;background:linear-gradient(180deg,#cfd5cc,#b9bfb3)"></section>
<h2 class="abs serif center" style="top:3448px;font-size:38px;font-weight:500;color:rgba(255,255,255,.75)">GET IN TOUCH</h2>
<div class="field" style="left:165px;top:3528px;width:283px;height:48px">Full Name</div>
<div class="field" style="left:458px;top:3528px;width:283px;height:48px">Phone Number</div>
<div class="field" style="left:751px;top:3528px;width:284px;height:48px">Email Address</div>
<div class="field" style="left:165px;top:3590px;width:870px;height:95px">Message...!</div>
<div class="btn" style="left:518px;top:3700px;width:164px;height:48px;background:var(--white);color:#555;font-size:15px">Send Message</div>

<!-- Footer -->
<div class="abs brand center" style="top:3860px;font-size:38px">Dora Beckett</div>
<div class="abs center foot-nav"><span>HOME</span><span>/</span><span>WORK WITH ME</span><span>/</span><span>PRAISE</span><span>/</span><span>ABOUT</span><span>/</span><span>PODCAST</span></div>
<div class="abs center" style="top:3978px;font-size:13px;color:#666">
  <svg width="12" height="12" viewBox="0 0 24 24" style="vertical-align:-1px"><path fill="#e9a3ae" d="M6.6 10.8a15 15 0 006.6 6.6l2.2-2.2c.3-.3.7-.4 1-.2 1.1.4 2.3.6 3.6.6.6 0 1 .4 1 1V20c0 .6-.4 1-1 1A17 17 0 013 4c0-.6.4-1 1-1h3.5c.6 0 1 .4 1 1 0 1.3.2 2.5.6 3.6.1.3 0 .7-.2 1z"/></svg>
  &nbsp;+1 (555) 014 2290 &nbsp;&nbsp; / &nbsp;&nbsp;
  <svg width="13" height="10" viewBox="0 0 26 20" style="vertical-align:0"><rect x="1" y="1" width="24" height="18" rx="2" fill="#e9a3ae"/><path d="M2 2l11 9 11-9" stroke="#fff" stroke-width="2" fill="none"/></svg>
  &nbsp;hello@dorabeckett.com
</div>
<div class="abs center socials"><span></span><span></span><span></span><span></span><span></span></div>
<div class="abs" style="left:112px;top:4068px;width:976px;height:1px;background:#e3e3e3"></div>
<div class="abs" style="left:476px;top:4090px;font-size:12px;color:#888">© 2022 Dora Beckett &nbsp; / &nbsp; All Rights Reserved</div>
<div class="abs" style="left:828px;top:4090px;font-size:12px;color:var(--mauve)">Privacy Policy &nbsp;/&nbsp; Terms Of Use &nbsp;/&nbsp; Disclaimer</div>

</body>
</html>
```